Brindle Children's Center - Child Care brochure

I just bought a new child care and completely renovated the space. We are also designing a new website, so I need the brochure to match that with updated info. www.brindlechildrenscenter.com - Information on there is current. We expect to have the new one up and running in the next few days. We have new photo's that I'd like to be added to the flyer too. ps. the boys in the pictures are mine, so i would appreciate one of them being added :). support@pixelhavenweb.com has details on the website (dev.brindlechildrenscenter.com). The child care program is only open during the ski season - i.e. a resort facility catering to high end clients.
I'm attaching the the website information, the flyer I created, logo files and pictures.

dev.brindlechildrenscenter.com Added Sunday, September 24, 2017

Target Market(s)

Parents of young children

Font styles to use
Other font styles liked:
• "Things we said" & "Calibri Light"

Colors
cfeae6
fef1ee

Requirements
Must have
• Pictures of children. sleek design - winter, mountain theme. Check with website designer on new website.
Nice to have
• prices included
Should not have
• Kid like artwork

```html
<!DOCTYPE html>
<html lang="en">
<head>
<meta charset="utf-8">
<title>Brindle Children's Center – Brochure</title>
<link href="https://fonts.googleapis.com/css2?family=Fredoka:wght@400;500&family=Open+Sans:wght@400;600&display=swap" rel="stylesheet">
<style>
:root{
  --orange:#ef7552;
  --teal:#4f8e85;
  --teal-dark:#3f7a71;
  --ink:#2e2e2e;
  --body:#3c3c3c;
  --paper:#ffffff;
  --snow:#eef1f6;
  --backdrop:#e6e6e6;
  --night:rgba(38,46,62,.86);
}
*{margin:0;padding:0;box-sizing:border-box}
html,body{width:1200px;height:1200px;overflow:hidden;background:var(--backdrop)}
body{position:relative;font-family:"Open Sans",sans-serif;color:var(--body)}
.spread{position:absolute;left:205px;width:790px;height:563px;background:var(--paper);overflow:hidden}
.spread--outside{top:24px}
.spread--inside{top:613px}
.abs{position:absolute}
.photo{position:absolute;overflow:hidden}
.fold{position:absolute;top:0;bottom:0;width:1px;background:rgba(0,0,0,.06)}
.heading{font-family:"Fredoka",sans-serif;font-weight:500;color:var(--orange)}
.copy{font-size:7.6px;line-height:1.45;text-align:justify}
.circle{position:absolute;border-radius:50%;border:5px solid var(--paper)}
.circle--orange{box-shadow:-5px 3px 0 0 var(--orange)}
.circle--teal{box-shadow:5px 3px 0 0 var(--teal)}
.brand-mark{position:absolute;display:flex;align-items:center;gap:6px;font-family:"Fredoka",sans-serif;font-weight:500;color:var(--ink);white-space:nowrap}
.brand-mark .dot{width:10px;height:10px;border:1.5px solid var(--ink);border-radius:50%}

/* outside left */
.reserve-box{left:0;top:60px;width:254px;height:164px;background:var(--night);border-radius:0 14px 0 0;padding:14px 14px 0 20px;color:#fff}
.reserve-box h3{font-size:12px;letter-spacing:.2px;margin-bottom:3px}
.reserve-box p{font-size:7.4px;line-height:1.4;text-align:justify;margin-bottom:6px}
.rates{left:20px;top:290px;width:230px}
.rates h3{font-family:"Fredoka",sans-serif;font-weight:400;color:var(--teal);font-size:12px;margin-bottom:2px}
.rate-row{display:flex;font-size:7.4px;line-height:1.5;padding-bottom:4px;margin-bottom:4px;border-bottom:1px solid #c9ccd3}
.rate-row:last-child{border-bottom:none}
.rate-label{width:115px;color:var(--orange)}
.rate-list{color:var(--teal)}
.rate-list b{font-weight:600}
/* outside middle */
.contact{left:265px;top:443px;width:263px;text-align:center;font-size:9px;line-height:1.9;color:var(--ink)}
.contact span{display:inline-flex;align-items:center;gap:5px}
.open-pill{left:330px;top:522px;width:146px;height:20px;border-radius:10px;background:var(--orange);color:#fff;font-size:10.5px;font-weight:600;text-align:center;line-height:20px}
/* outside right */
.serving{position:absolute;left:528px;top:420px;width:262px;text-align:center;font-family:"Fredoka",sans-serif;color:var(--ink);font-size:18px;letter-spacing:-.3px}
.ages{position:absolute;left:528px;top:449px;width:262px;text-align:center;font-family:"Fredoka",sans-serif;font-weight:500;color:var(--teal);font-size:17px;letter-spacing:1px}
.rule{left:585px;top:483px;width:152px;height:1px;background:#777}
.located{position:absolute;left:556px;top:493px;width:206px;text-align:center;color:var(--orange);font-size:11px;line-height:1.4}

/* inside */
.welcome{position:absolute;left:32px;top:26px;color:var(--orange);font-family:"Fredoka",sans-serif;font-weight:500;font-size:14px;line-height:1.2}
.welcome span{color:#fff}
.list{list-style:none;font-family:"Fredoka",sans-serif;font-size:9.5px;line-height:1.32;color:var(--ink)}
.list li::before{content:"· ";color:var(--teal)}
.sub{font-family:"Fredoka",sans-serif;font-weight:400;color:var(--orange);font-size:13px;margin:6px 0 3px}
.cloud-label{font-family:"Fredoka",sans-serif;font-weight:500;color:#fff;font-size:14px;letter-spacing:.3px}
.bring{list-style:none}
.bring li{position:relative;padding-left:12px;margin-bottom:5px}
.bring li::before{content:"";position:absolute;left:2px;top:4px;width:3px;height:3px;border-radius:50%;background:var(--teal)}
.teal-text{color:var(--teal);font-weight:600}
</style>
</head>
<body>

<section class="spread spread--outside" aria-label="Brochure outside">
  <div class="photo" style="left:0;top:0;width:790px;height:300px;background:linear-gradient(180deg,#7f93b8 0%,#c9d3e4 30%,#e8edf4 62%,#f3f5f9 100%)" role="img" aria-label="Snowy mountain slopes with pine trees and ski lodge"></div>
  <div class="photo" style="left:265px;top:0;width:263px;height:300px;background:linear-gradient(180deg,#8193b6 0%,#a9b6cc 35%,#5b6b62 55%,#d9dfea 75%,#f4f6fa 100%)" role="img" aria-label="Ski run lined with pine trees under snowy peaks"></div>
  <div class="photo" style="left:528px;top:0;width:262px;height:300px;background:linear-gradient(160deg,#9aa8c4 0%,#b27a55 35%,#c08a66 55%,#dfe3ea 80%,#f4f6fa 100%)" role="img" aria-label="Ski lodge building with visitors in the snow"></div>
  <div class="abs" style="left:0;top:300px;width:790px;height:263px;background:linear-gradient(180deg,#f4f6fa,#fbfbfd)"></div>
  <svg class="abs" style="left:265px;top:180px" width="525" height="130" viewBox="0 0 525 130"><path d="M0 50 Q130 100 263 60 L263 130 L0 130Z" fill="#f8f9fb"/><path d="M263 80 Q390 120 525 70 L525 130 L263 130Z" fill="#f8f9fb"/></svg>
  <div class="fold" style="left:265px"></div>
  <div class="fold" style="left:528px"></div>

  <div class="abs reserve-box">
    <h3 class="heading">RESERVATIONS</h3>
    <p>Your reservation fee will be applied to your last day of service.</p>
    <p>We highly recommend that reservations be made in advance to ensure space for your child. To make a reservation contact us at: 801-555-0142. We have limited capacity.</p>
    <h3 class="heading">CANCELLATION POLICY</h3>
    <p>Reservations must be cancelled 24hrs in advance of the date(s) of service or full fee will be charged for all days not cancelled</p>
  </div>

  <div class="abs rates">
    <h3>RATES</h3>
    <div class="rate-row"><div class="rate-label">Infant/Toddler/.................</div><div class="rate-list"><b>$105</b>/full day<br><b>$90</b>/half day<br><b>$475</b>/Five day package</div></div>
    <div class="rate-row"><div class="rate-label">3 years and Up:.................</div><div class="rate-list"><b>$99</b>/full day<br><b>$85</b>/half day<br><b>$450</b>/Five day package</div></div>
  </div>

  <div class="photo" style="left:0;top:405px;width:270px;height:158px;background:radial-gradient(circle at 55% 40%,#c79b6c 0%,#a9825c 40%,#6c5849 75%,#3a3534 100%);clip-path:polygon(0 35%,40% 0,100% 20%,100% 100%,0 100%)" role="img" aria-label="Baby reading a picture book with a parent beside a large teddy bear"></div>

  <div class="circle circle--orange" style="left:309px;top:201px;width:105px;height:105px;background:linear-gradient(135deg,#d8c59c,#b98a5c)" role="img" aria-label="Toddler playing at a play table"></div>
  <div class="circle circle--teal" style="left:409px;top:202px;width:118px;height:118px;background:linear-gradient(135deg,#e3b9c6,#b6648a)" role="img" aria-label="Girl drawing with colored markers"></div>

  <div class="brand-mark" style="left:332px;top:367px;font-size:11px"><span class="dot"></span>Brindle Children's Center</div>

  <div class="abs contact">
    <span><svg width="9" height="9" viewBox="0 0 24 24"><path fill="#4f8e85" d="M6.6 10.8a15 15 0 006.6 6.6l2.2-2.2c.3-.3.7-.4 1-.2 1.1.4 2.3.6 3.6.6.6 0 1 .4 1 1V20c0 .6-.4 1-1 1A17 17 0 013 4c0-.6.4-1 1-1h3.5c.6 0 1 .4 1 1 0 1.3.2 2.5.6 3.6.1.3 0 .7-.2 1z"/></svg>(801) 555-0142</span><br>
    <span><svg width="9" height="9" viewBox="0 0 24 24"><circle cx="12" cy="12" r="10" fill="none" stroke="#4f8e85" stroke-width="2.5"/><path d="M7 10h10M7 14h10" stroke="#4f8e85" stroke-width="2.5"/></svg>info@brindlechildrenscenter.com</span><br>
    <span><svg width="9" height="9" viewBox="0 0 24 24"><circle cx="12" cy="12" r="10" fill="#4f8e85"/><path d="M2 12h20M12 2c3 3 3 17 0 20M12 2c-3 3-3 17 0 20" stroke="#fff" stroke-width="1.5" fill="none"/></svg>www.brindlechildrenscenter.com</span><br>
    <span>P.O. Box 4120 Brindle, Utah 84000</span>
  </div>
  <div class="abs open-pill">Open daily: 8:30-4:30</div>

  <div class="circle circle--orange" style="left:566px;top:172px;width:112px;height:112px;background:linear-gradient(135deg,#d6b7b0,#9b6d78)" role="img" aria-label="Children dressing up and playing together"></div>
  <div class="circle circle--teal" style="left:681px;top:201px;width:105px;height:105px;background:linear-gradient(135deg,#dfe4ec,#a9b4c7)" role="img" aria-label="Girl drawing on a whiteboard"></div>

  <div class="brand-mark" style="left:594px;top:355px;font-size:12px"><span class="dot"></span>Brindle Children's Center</div>
  <div class="serving">SERVING CHILDREN AGES</div>
  <div class="ages">6 WKS THRU 9 YEARS</div>
  <div class="abs rule"></div>
  <div class="located">(Located at the Ridgeview Ticket Office Building)</div>
</section>

<section class="spread spread--inside" aria-label="Brochure inside">
  <div class="fold" style="left:265px"></div>
  <div class="fold" style="left:528px"></div>

  <svg class="abs" style="left:0;top:0" width="265" height="115" viewBox="0 0 265 115">
    <path d="M0 0H258 Q250 40 225 62 Q190 86 140 74 Q100 66 70 82 Q30 102 0 112Z" fill="#ef7552"/>
    <path d="M0 0H252 Q244 36 220 57 Q188 80 140 69 Q98 60 66 77 Q30 96 0 106Z" fill="#4f8e85"/>
  </svg>
  <div class="welcome">WELCOME TO THE BRINDLE<br><span>CHILDREN'S CENTER!</span></div>

  <div class="abs" style="left:32px;top:125px;width:213px">
    <p class="copy">When you hit the slopes you want to make sure your child has a great day too. At the Brindle Children's Center you can be sure that your child receives the best care possible – and has a great time to boot! Located on the slopes of world famous Brindle Peak Resort, you can drop off your child at a safe, and fun center and step out the door to the slopes.</p>
    <h3 class="heading" style="font-size:14px;font-weight:400;margin:9px 0 3px">OUR SERVICES</h3>
    <p class="copy">The Brindle Children's Center is a full service childcare facility that caters to children from six weeks to nine years old. Infants, toddlers, and young children can explore the activities and toys available in the Center. Children ages four and older have the option to join Brindle's legendary Halvorsen Ski School and spend part or all of the day learning from one of Brindle's friendly instructors.</p>
    <p class="copy" style="margin-top:6px">Children visiting the center can look forward to the following activities:</p>
    <ul class="list" style="margin-top:14px;margin-left:6px">
      <li>Dramatic play</li><li>Arts and Crafts</li><li>Discovery Science</li><li>Snow Play</li><li>Games</li><li>Music</li><li>Nutritious lunch and snacks</li>
    </ul>
  </div>
  <div class="photo" style="left:0;top:472px;width:265px;height:91px;background:linear-gradient(90deg,#c59b7a,#9d8c8a 50%,#6f8a86);clip-path:polygon(0 8%,70% 0,100% 55%,100% 100%,0 100%)" role="img" aria-label="Children doing crafts together at a classroom table"></div>

  <svg class="abs" style="left:255px;top:0" width="205" height="80" viewBox="0 0 205 80">
    <g fill="#ef7552"><ellipse cx="100" cy="38" rx="90" ry="28"/><circle cx="30" cy="30" r="22"/><circle cx="70" cy="18" r="24"/><circle cx="125" cy="16" r="24"/><circle cx="170" cy="30" r="24"/><circle cx="50" cy="52" r="18"/><circle cx="150" cy="54" r="18"/><circle cx="12" cy="40" r="12"/></g>
  </svg>
  <div class="abs cloud-label" style="left:302px;top:28px">OUR PROGRAM</div>

  <div class="abs" style="left:298px;top:82px;width:215px">
    <p class="copy">The Brindle Children's Center is fully accredited by the State of Utah and offers a program that caters to your child's needs:</p>
    <h4 class="sub">Infant Care</h4>
    <p class="copy">Our infant care program is open to children over six weeks. We will tailor a program to meet your child's daily schedule. Pagers are available for nursing mothers and concerned parents.</p>
    <h4 class="sub">Toddlers</h4>
    <p class="copy">Children ages 18-months to three years want to explore just about everything! Creative art projects, musical games, and large muscle activities will keep your little one active and happy all day.</p>
    <h4 class="sub">Ages Three and Up</h4>
    <p class="copy">With their teacher and new friends, your child will explore the wonder of Brindle snow, enjoy art projects, and choose from a variety of activities that challenge the imagination.</p>
    <h4 class="sub">Ski School</h4>
    <p class="copy">The Brindle Children's Center works closely with the famous Halvorsen Ski School. If you wish to have your child (ages 4 and up) participate in a group ski lesson, we will take your child to meet their ski class and pick them up after. Private lessons are also available for any age.</p>
  </div>
  <div class="circle circle--orange" style="left:296px;top:461px;width:115px;height:115px;background:linear-gradient(135deg,#f1d27a,#c59f52)" role="img" aria-label="Girl in a dress-up costume holding a doll"></div>
  <div class="circle circle--teal" style="left:402px;top:451px;width:125px;height:125px;background:linear-gradient(135deg,#e6e0da,#4f6f74)" role="img" aria-label="Boy and toddler playing together"></div>

  <div class="photo" style="left:540px;top:0;width:250px;height:166px;background:linear-gradient(90deg,#2f3a52 0%,#4c5b78 30%,#dfe1e4 45%,#eceef0 100%)" role="img" aria-label="Smiling boy sitting by a wall quote about curious children"></div>
  <div class="abs" style="left:540px;top:166px;width:250px;height:13px;background:var(--orange)"></div>
  <svg class="abs" style="left:553px;top:152px" width="165" height="72" viewBox="0 0 165 72">
    <g fill="#4f8e85"><ellipse cx="82" cy="38" rx="72" ry="24"/><circle cx="26" cy="32" r="20"/><circle cx="60" cy="18" r="20"/><circle cx="104" cy="16" r="20"/><circle cx="140" cy="30" r="20"/><circle cx="44" cy="54" r="14"/><circle cx="124" cy="54" r="14"/></g>
  </svg>
  <div class="abs cloud-label" style="left:585px;top:182px">OUR STAFF</div>

  <div class="abs" style="left:558px;top:240px;width:212px">
    <p class="copy">At the Brindle Children's Center our staff takes pride in creating a nurturing and creative atmosphere where your child can learn and grow. Each member of our staff is continuously trained in Early Childhood Education, CPR and first aid. We work together as a team to provide the best care possible for your child.</p>
    <h4 class="sub" style="margin:8px 0 8px">Things to bring with you:</h4>
    <ul class="bring copy">
      <li>For Infants, parents should supply diapers, wipes, a change of clothes, strained food (yum), and formula.</li>
      <li>For Toddlers, parents should supply diapers, wipes, and a change of clothes.</li>
      <li>For Ages 3 and Up, parents should supply a change of clothes, snow gear including: coat, hat, gloves, and snow pants, boots, and eye protection (sun glasses or goggles).</li>
    </ul>
    <h4 class="sub" style="margin:12px 0 8px">Reservations</h4>
    <p class="copy" style="text-align:left">We highly recommend that reservations be made in advance to ensure space for your child. To make a reservation <span class="teal-text">contact us at: 801-555-0142.</span><br>We have limited capacity.</p>
  </div>
</section>

</body>
</html>
```